A4 Flyer folded into DL size for Solar Power

We need a design for a A4 sized flyer folded into a DL sized flyer. We are a Sydney based Solar sales, design and installation company called 'Vantrel Solar'.
This flyer is designed to inform and educate the general public on how much saving they can make by installing Solar panels on top of their household roof.
I already have the texts of the flyer copywritten, so all i need is the design.
Since the flyer is folded from A4 to DL size, there will be six faces, I've labelled and attached the documents for the layouts.

You can take any picture from our website: www.vantrelsolar-example.com.au
I've also attached a few pictures, but if that's not enough please add your own.

If you want some reference, our current website is www.vantrelsolar-example.com.au

Target Market(s)

Adults of Metro Sydney aged between 35-60 which own houses, and want to make savings on the their everyday electricity expenses.

Industry/Entity Type

It Company

Requirements
Should not have
• Do not put the Logo on the front of the brochure.

```html
<!DOCTYPE html>
<html lang="en">
<head>
<meta charset="utf-8">
<title>Vantrel Solar – DL Flyer Inside Spread</title>
<link href="https://fonts.googleapis.com/css2?family=Roboto+Condensed:wght@400;700&display=swap" rel="stylesheet">
<style>
  :root {
    --white: #ffffff;
    --ink: #1d1d1f;
    --red: #e1261c;
    --orange: #ee7b1d;
    --yellow: #f6e71c;
    --panel-blue-dark: #0d3f86;
    --panel-blue: #2d74c4;
    --sky-top: #0f4fb0;
    --sky-mid: #5c9ee0;
    --field: #5f7d2c;
    --field-dark: #3e5a1c;
    --olive-box: rgba(72, 84, 32, 0.78);
    --roof: #8e2a20;
    --divider: #f4f4f4;
  }
  * { box-sizing: border-box; margin: 0; padding: 0; }
  html, body { width: 1200px; height: 931px; overflow: hidden; background: var(--white); }
  body { font-family: "Roboto Condensed", "Arial Narrow", sans-serif; color: var(--ink); }

  .spread { position: relative; width: 1200px; height: 931px; background: var(--divider); }
  .panel { position: absolute; top: 0; height: 931px; overflow: hidden; }
  .panel--savings { left: 0; width: 393px; }
  .panel--subsidies { left: 398px; width: 387px; }
  .panel--risks { left: 789px; width: 411px; background: var(--white); }

  .photo { position: absolute; }
  .photo--solar-array {
    inset: 0;
    background: linear-gradient(160deg, var(--panel-blue-dark) 0%, var(--panel-blue) 35%, #6fa3de 55%, var(--panel-blue) 75%, var(--panel-blue-dark) 100%);
  }
  .photo--sky-field {
    inset: 0;
    background: linear-gradient(180deg, var(--sky-top) 0%, var(--sky-mid) 30%, #d9e8f5 42%, #9cb8d0 52%, var(--field) 78%, var(--field-dark) 100%);
  }
  .photo--roof {
    left: 0; right: 0; bottom: 0; height: 296px;
    background: linear-gradient(170deg, #6f9a4a 0%, #b8cad6 18%, var(--roof) 40%, #a63a2a 70%, #6b1f17 100%);
  }

  .headline {
    position: absolute; color: var(--white); font-weight: 700;
    font-size: 16.5px; line-height: 1.3;
  }
  .panel--savings .headline { left: 40px; top: 144px; width: 340px; }

  .savings-card {
    position: absolute; left: 0; top: 228px; width: 384px; height: 606px;
    background: var(--white); padding: 24px 14px 0 14px;
    font-size: 15px; line-height: 1.3;
  }
  .savings-card p { margin-bottom: 18px; }
  .callout { color: var(--red); font-weight: 700; }
  .testimonial h3 { font-size: 15px; font-weight: 700; }
  .testimonial { margin-bottom: 20px; }
  .testimonial .author { color: var(--orange); font-weight: 700; display: block; }
  .testimonial p { margin-bottom: 0; }

  .panel--subsidies .headline { left: 0; width: 387px; top: 58px; text-align: center; font-size: 16.5px; }
  .intro {
    position: absolute; left: 17px; top: 90px; width: 355px;
    color: var(--white); font-weight: 700; font-size: 15.5px; line-height: 1.3;
  }
  .subsidy-box {
    position: absolute; left: 10px; top: 304px; width: 371px; height: 426px;
    background: var(--olive-box); color: var(--white);
    padding: 8px 6px; font-size: 15px; line-height: 1.3;
  }
  .subsidy-box p { margin-bottom: 19px; }
  .subsidy-box strong { color: var(--yellow); }

  .risks-title {
    position: absolute; left: 0; width: 411px; top: 118px; text-align: center;
    color: var(--red); font-weight: 700; font-size: 17px;
  }
  .risks-title .mark { color: var(--orange); font-size: 46px; line-height: 0; vertical-align: -2px; margin-left: 2px; }
  .risks-copy {
    position: absolute; left: 37px; top: 240px; width: 355px;
    font-size: 15px; line-height: 1.3;
  }
  .risks-copy p { margin-bottom: 19px; }
  .risks-copy .answer { font-weight: 700; margin-bottom: 24px; }
  .risks-copy strong { color: var(--red); }
  .accent-stripes { position: absolute; right: 0; top: 0; width: 60px; height: 600px; }
</style>
</head>
<body>
<main class="spread">

  <section class="panel panel--savings">
    <div class="photo photo--solar-array" role="img" aria-label="Close-up of blue solar panel cells"></div>
    <h2 class="headline">Yes, you can beat the energy price hikes and AS A BONUS have your electricity company PAY YOU every time you get a bill.</h2>
    <div class="savings-card">
      <p>All you have to do is take advantage of the Federal and State Government solar subsidy and rebate schemes and you're on your way to making massive savings on your power bills.</p>
      <p class="callout">Here's what home owners who've taken action to beat soaring electricity costs say about the effect it's had on their hip pockets.</p>
      <div class="testimonial">
        <h3>Power bills slashed by 75%</h3>
        <p>‘With a five person family, our electricity bills were regularly costing us $400 a quarter and there was no way I wanted to pay more. Since getting Vantrel Solar to install our solar electricity system the bills have dropped to just $100 a quarter.’</p>
        <span class="author">Marcus Tenley, Carlingford, NSW</span>
      </div>
      <div class="testimonial">
        <p><strong>We've saved $430 per quarter</strong>&nbsp; ‘When our electricity bills hit $500 a quarter we decided to look seriously at the solar rebate scheme. Since Vantrel Solar put in our system, our bill has dropped to only $70. It's amazing. They took care of everything, including the rebate applications.’</p>
        <span class="author">Priya Hollis, Bankstown, NSW</span>
      </div>
    </div>
  </section>

  <section class="panel panel--subsidies">
    <div class="photo photo--sky-field" role="img" aria-label="Blue sky with white clouds over a grassy field with solar panels"></div>
    <h2 class="headline">Here's how you can shrink your electricity bills</h2>
    <p class="intro">As a home owner, you are entitled to take advantage of two government subsidies aimed at encouraging Australians to help cut greenhouse gas emissions.</p>
    <div class="subsidy-box">
      <p><strong>The first subsidy</strong> is for the purchase and installation of a home solar electricity system.</p>
      <p><strong>The second subsidy</strong> is a rebate scheme in which you sell ALL the power produced by your solar electricity system to your electricity company at a premium rate.</p>
      <p><strong>The money you make</strong> from selling your solar electricity to your electricity company is taken off the cost of your household electricity bill.</p>
      <p><strong>Imagine $0 bills.</strong> Depending on how much solar electricity you generate, you could quickly find your electricity bills are in credit. This means while other people are struggling to pay their bills, you can relax with nothing to pay for your household energy use.</p>
    </div>
  </section>

  <section class="panel panel--risks">
    <svg class="accent-stripes" viewBox="0 0 60 600" aria-hidden="true">
      <rect x="10" y="0" width="6" height="600" fill="#f6d9bf" opacity="0.6"/>
      <rect x="26" y="0" width="10" height="600" fill="#f3c9a3" opacity="0.5"/>
      <rect x="44" y="0" width="6" height="600" fill="#f6d9bf" opacity="0.6"/>
    </svg>
    <h2 class="risks-title">Are there any risks<span class="mark">?</span></h2>
    <div class="risks-copy">
      <p class="answer">No, there are no risks to you or your home.</p>
      <p><strong>The rebate scheme</strong>, called the Solar Bonus Scheme, is fully legislated by the NSW Government, so it's guaranteed you'll be paid for generating solar power for the life of the scheme.</p>
      <p><strong>When you choose us</strong>, Vantrel Solar, as your supplier and installer, you will receive only quality, fully warranted products from world-leading manufacturers.</p>
      <p><strong>All Vantrel Solar installers</strong> are fully licensed reliable electricians also accredited by the Clean Power Accreditation Board and operating to Australian Standards.</p>
    </div>
    <div class="photo photo--roof" role="img" aria-label="Solar panel mounted on a red tiled house roof with chimney and trees"></div>
  </section>

</main>
</body>
</html>
```